Birchlane Chiropractic Business Cards

Business cards with new logo design. Will upload copy of current card. We like the layout, but we need a new logo. Family, husband holding up baby toward sky, mom and other child standing next to him. We will probably want to include a catch phrase with logo. TBD

```html
<!DOCTYPE html>
<html lang="en">
<head>
<meta charset="utf-8">
<title>Birchlane Chiropractic – Folded Business Card</title>
<link rel="stylesheet" href="https://fonts.googleapis.com/css2?family=Montserrat:ital,wght@0,400;0,500;0,600;1,400&display=swap">
<style>
  :root {
    --backdrop: #c5cacc;
    --card-red: #ef232d;
    --card-white: #e2e2e2;
    --ink: #141414;
    --paper: #ffffff;
    --illustration-tone: #cfcfcf;
    --map-tone: #f4f4f4;
  }
  * { box-sizing: border-box; margin: 0; padding: 0; }
  html, body { width: 936px; height: 1200px; overflow: hidden; }
  body {
    background: var(--backdrop);
    font-family: "Montserrat", sans-serif;
    color: var(--ink);
    position: relative;
  }
  .spread {
    position: absolute;
    left: 248px;
    width: 440px;
    height: 385px;
    display: flex;
    box-shadow: 0 10px 24px rgba(0,0,0,0.18);
  }
  .spread--outside { top: 110px; }
  .spread--inside { top: 680px; }
  .panel { width: 220px; height: 385px; position: relative; }
  .panel--red { background: var(--card-red); color: var(--paper); }
  .panel--white { background: var(--card-white); }

  /* outside front */
  .cover-name {
    position: absolute;
    left: 50%; top: 50%;
    transform: translate(-50%, -50%) rotate(90deg);
    white-space: nowrap;
    text-align: center;
    font-weight: 600;
    font-size: 22px;
    line-height: 1.15;
    letter-spacing: 0.5px;
    color: var(--ink);
  }

  /* inside left */
  .illustration {
    position: absolute;
    left: 16px; top: 18px;
    width: 188px; height: 188px;
    border: 1px solid var(--card-red);
    border-radius: 14px;
    background: radial-gradient(circle at 50% 55%, var(--illustration-tone), var(--card-white) 75%);
  }
  .identity {
    position: absolute;
    left: 0; right: 0; top: 222px;
    text-align: center;
  }
  .identity__name {
    font-weight: 600;
    font-size: 16px;
    line-height: 1.2;
    letter-spacing: 0.3px;
    color: var(--ink);
  }
  .identity__doctor { margin-top: 20px; font-size: 11px; }
  .identity__role { font-size: 8.5px; font-style: italic; margin-top: 3px; }
  .identity__phone { margin-top: 14px; font-size: 11px; font-style: italic; }
  .identity__web { margin-top: 6px; font-size: 10.5px; }

  /* inside right */
  .map {
    position: absolute;
    left: 14px; top: 30px;
    width: 192px; height: 188px;
    background: var(--map-tone);
    border-radius: 14px;
  }
  .address {
    position: absolute;
    left: 0; right: 0; top: 238px;
    text-align: center;
    font-size: 9.5px;
    line-height: 1.45;
  }
</style>
</head>
<body>
  <section class="spread spread--outside" aria-label="Card outside">
    <div class="panel panel--red"></div>
    <div class="panel panel--white">
      <p class="cover-name">BIRCHLANE<br>CHIROPRACTIC</p>
    </div>
  </section>

  <section class="spread spread--inside" aria-label="Card inside">
    <div class="panel panel--white">
      <div class="illustration" role="img" aria-label="Silhouette of a family: father lifting a baby skyward, mother and child standing beside him"></div>
      <div class="identity">
        <p class="identity__name">BIRCHLANE<br>CHIROPRACTIC</p>
        <p class="identity__doctor">Dr. Daniel R. Fenwick</p>
        <p class="identity__role">Chiropractic Physician</p>
        <p class="identity__phone">555-214-0386</p>
        <p class="identity__web">FenwickChiro.com</p>
      </div>
    </div>
    <div class="panel panel--red">
      <div class="map" role="img" aria-label="Street map showing the clinic location between surrounding avenues and roads"></div>
      <p class="address">
        2480 SE Alder Grove Center Dr.<br>
        Maple Hollow, Oregon 97000<br>
        555 - 301 - 4470<br>
        Fax : 555 - 301 - 4471
      </p>
    </div>
  </section>
</body>
</html>
```